mosswickpartners Business Card Design

Business card with logo design for mosswickpartners. We are a group of professional project managers based on the Pareto Principle that 80% of the work is done by 20% of the people. I have a makeshift logo that uses a pi chart with 30% and 20% and the 20% pie slice is set slightly out and up. Have played around with a teal and orange colour scheme.

Industry/Entity Type

Business

Contact Information for Business Card

Harold Penbury
Director
mosswickpartners

0487 263019

```html
<!DOCTYPE html>
<html lang="en">
<head>
<meta charset="utf-8">
<title>mosswickpartners Business Card</title>
<link rel="stylesheet" href="https://fonts.googleapis.com/css2?family=Open+Sans:wght@400;600;700&display=swap">
<style>
  :root {
    --backdrop: #e6e6e6;
    --card: #ffffff;
    --teal: #1f8c93;
    --orange: #ef6f45;
    --ink: #2b2b2b;
    --ink-soft: #444444;
  }
  * { box-sizing: border-box; margin: 0; padding: 0; }
  html, body {
    width: 1200px; height: 900px; overflow: hidden;
    background: var(--backdrop);
    font-family: "Open Sans", Arial, sans-serif;
    color: var(--ink);
  }
  .sheet {
    width: 1200px; height: 900px;
    display: flex; flex-direction: column; align-items: center; justify-content: center;
    gap: 56px;
  }
  .card {
    position: relative;
    width: 630px; height: 360px;
    background: var(--card);
    box-shadow: 0 6px 18px rgba(0,0,0,0.12);
    overflow: hidden;
  }
  .brand { display: flex; align-items: center; gap: 14px; }
  .brand-dot {
    width: 52px; height: 52px; border-radius: 50%;
    background: var(--orange);
  }
  .brand-name {
    font-weight: 400; font-size: 30px; color: var(--teal); letter-spacing: 0.5px;
  }
  .card-back .brand {
    position: absolute; left: 50%; top: 50%; transform: translate(-50%, -50%);
  }
  .card-front .brand { position: absolute; left: 40px; top: 92px; }
  .holder { position: absolute; right: 40px; top: 34px; text-align: right; }
  .holder-name { font-weight: 700; font-size: 22px; color: var(--ink); }
  .holder-title { font-size: 14px; color: var(--ink-soft); margin-top: 2px; }
  .address {
    position: absolute; right: 40px; top: 112px; text-align: right;
    font-style: normal; font-size: 14px; line-height: 1.45; color: var(--ink-soft);
  }
  .swoosh { position: absolute; left: 0; top: 0; width: 630px; height: 360px; }
  .contacts {
    position: absolute; left: 40px; top: 228px; list-style: none;
    font-size: 14px; line-height: 1.4; color: var(--ink);
  }
  .contacts li { display: flex; align-items: center; gap: 8px; }
  .contacts svg { width: 12px; height: 12px; fill: var(--ink); }
</style>
</head>
<body>
<main class="sheet">
  <section class="card card-back">
    <div class="brand">
      <span class="brand-dot"></span>
      <span class="brand-name">mosswickpartners</span>
    </div>
  </section>

  <section class="card card-front">
    <svg class="swoosh" viewBox="0 0 630 360" aria-hidden="true">
      <path class="swoosh-band" d="M0 330 C 220 330, 330 284, 420 246 S 565 192, 630 188 L630 206 C 570 210, 470 242, 420 264 C 330 302, 220 346, 0 346 Z" fill="var(--orange)"/>
      <path class="swoosh-line" d="M0 320 C 220 320, 330 272, 420 234 S 560 178, 630 172" fill="none" stroke="var(--teal)" stroke-width="5"/>
    </svg>

    <div class="brand">
      <span class="brand-dot"></span>
      <span class="brand-name">mosswickpartners</span>
    </div>

    <div class="holder">
      <p class="holder-name">Harold Penbury</p>
      <p class="holder-title">Managing Director</p>
    </div>

    <address class="address">
      P.O Box 42 Fenwick St<br>
      Harlow Bay Country 318
    </address>

    <ul class="contacts">
      <li><svg viewBox="0 0 12 12"><path d="M2 1h2.5l1 3-1.5 1a7 7 0 0 0 3 3l1-1.5 3 1V10a1 1 0 0 1-1 1A9 9 0 0 1 1 2a1 1 0 0 1 1-1z"/></svg>0487 263019</li>
      <li><svg viewBox="0 0 12 12"><path d="M3 1h5v3H3zM1 5h10v6H1zM3 7h2v1H3zm4 0h2v1H7z"/></svg>0487 263019</li>
      <li><svg viewBox="0 0 12 12"><path d="M1 3h10v7H1zM1 3l5 4 5-4" fill="none" stroke="#2b2b2b" stroke-width="1.2"/></svg>hello@mosswick.com</li>
    </ul>
  </section>
</main>
</body>
</html>
```